Power Point Template Kalvoren sustainability consulting

Please note:
We are not looking for new design proposals anymore since we've already received templetes from two designers that we really like. We are currently discussing possible changes with them and will make a final decision soon. Thank you very much.

(find english description below)
We are a small German start-up that offers sustainability consulting. For presentations of results, our company presentation, proposals, lectures, etc., we need a PowerPoint template that matches our logo. We come from classic management consulting / strategy consulting and also deal with facts and figures in sustainability consulting. Therefore, the template should not be too fancy and should not only consist of photos. But it shouldn't be a completely sober template either. Our logo with the green leaves for sustainability (three leaves for KALvoren) and the white bar chart (with the dynamic swing upwards) reflects our attitude well, where we see ourselves on the range from playful to sober and classic to modern.

It might be nice for the template to include the shape of one of the leaves (from the logo). Also, the logo should appear in a corner of each slide. The colors from the logo (see appendix) should be partially reflected in the presentation. We can also imagine a gold-brown tone (see website www.kalvoren-consulting.example) or a coral tone as a contrast. (Attention - the website is not final yet).

For a first suggestion, it is sufficient to suggest three to four slides (cover sheet, chapter/separation slide, text slide, data slide). We will then mark drafts that we like. In total, we would then need about 6-10 more slide templates, e.g. about us, team, slide for a statement, 2-3 data charts (pie, bar, column), top 3 - 5 list, timeline, contact (more slides are welcome ).

We are a small German start-up offering sustainability consulting. We need a power point template for result presentations, our company presentation, proposals, lectures etc. The template should be aligned with our logo. Our background lies in classic management consulting / strategy consulting and we also deal with facts and figures in sustainability consulting. Therefore, the template should not be too playful and not only consist of photos. But it should also not be a completely clear template. Our logo with the green leaves for sustainability (three leaves for KALvoren) and the white bar chart (with the dynamic upward swing) reflects our attitude well, where we see ourselves on the range from playful to down-to-earth and classic to modern .

For the template, it might be nice to incorporate the shape of one of the leaves (from the logo). Also, the logo should show up in one corner on each slide. Some of the colors from the logo (see attachment) should be reflected in the presentation. We could also think of a gold-brown tone (see website www.kalvoren-consulting.example) or a coral tone for contrast. (Attention - the website is not final yet).

For a first proposal it is quite sufficient to suggest us three to four slides (cover page, chapter/separation slide, text slide, data slide). We will then mark the drafts that we like. In total we would need about 6-10 more slide templates, eg About us, Team, slide for a statement, 2-3 data charts (pie, bar, column), Top 3 - 5 List, Timeline, Contact (more slides are welcome).

Target Market(s)

Corporations, large companies and SMEs

Industry/Entity Type

Unternehmensberatung, Nachhaltigkeitsberatung

Font styles to use
Sans Serif
Other font styles liked:
• Calibri

Colors
00AB8E
00BBA5
67D7C9
C6EFE9
E9F9F6

Requirements
Must have
• see description (e.g. the colors of our logo)
Nice to have
• see description (e.g. elements of the logo included)
Should not have
• see description

```html
<!DOCTYPE html>
<html lang="en">
<head>
<meta charset="utf-8">
<title>Kalvoren Consulting – Presentation Template</title>
<link rel="stylesheet" href="https://fonts.googleapis.com/css2?family=Fira+Sans+Condensed:wght@400;500;600&family=Open+Sans:wght@400&display=swap">
<style>
:root{
  --board:#c9c9c9;
  --teal:#17a07d;
  --teal-dark:#0f7d62;
  --mint:#caf2ec;
  --mint-pale:#e4f8f4;
  --gold:#b39a55;
  --ink:#1d1d1d;
  --grey-ink:#555a5e;
  --panel-grey:#e6e7e8;
  --blush:#fbefee;
  --g1:#2f5a12;--g2:#4a8020;--g3:#8bb833;--g4:#b5d56a;--g5:#cfe26a;
}
*{box-sizing:border-box;margin:0;padding:0}
html,body{width:1200px;height:4283px;overflow:hidden}
body{background:var(--board);position:relative;font-family:"Fira Sans Condensed",sans-serif;color:var(--ink)}
.slide{position:absolute;left:23px;width:1152px;height:648px;overflow:hidden;background:#fff;box-shadow:0 2px 6px rgba(0,0,0,.25)}
.abs{position:absolute}
.brand{font-family:"Open Sans",sans-serif;font-weight:400;color:var(--grey-ink);line-height:1}
.brand-dot{display:inline-block;border-radius:50%;background:var(--teal);vertical-align:middle}
.brand-sub{font-family:"Open Sans",sans-serif;color:var(--grey-ink);letter-spacing:1px}
/* cover */
.cover-band{left:0;top:0;width:120px;height:648px;background:var(--teal)}
.cover-top{left:120px;top:0;width:586px;height:58px;background:var(--mint-pale)}
.cover-photo{left:706px;top:0;width:446px;height:648px;background:linear-gradient(135deg,#2d8f78,#14634f 60%,#0d4a3b)}
.cover-wave{left:190px;top:235px;width:516px;height:150px;background:linear-gradient(180deg,rgba(179,154,85,0),rgba(179,154,85,.18),rgba(179,154,85,0))}
.welcome{left:158px;top:500px;font-size:30px;color:var(--ink)}
.welcome strong{display:block;font-size:42px;font-weight:600;color:var(--teal);line-height:1.05}
/* about */
.about-bg{left:0;top:0;width:1152px;height:648px;background:linear-gradient(160deg,#4fb8a2,#2a917b 50%,#67c8b5)}
.about-card{left:60px;top:60px;width:1033px;height:525px;background:var(--blush);border-radius:0 0 60px 60px}
.skyline{left:90px;top:460px;width:973px;height:110px;background:linear-gradient(180deg,rgba(201,168,100,.15),rgba(201,168,100,.55))}
.about-box{left:35px;top:111px;width:1087px;height:287px;background:var(--panel-grey);box-shadow:0 2px 5px rgba(0,0,0,.15);text-align:center}
.about-box h2{margin-top:50px;font-size:37px;font-weight:500}
.about-box h2 span{color:var(--teal)}
.about-box p{width:940px;margin:22px auto 0;font-size:15.5px;line-height:36px;color:#333}
/* team */
.team-band{left:0;top:131px;width:1152px;height:60px;background:var(--gold);color:#fff;font-size:36px;font-weight:500;text-align:center;line-height:60px}
.member{width:260px;height:246px;top:314px;background:var(--mint)}
.avatar{width:145px;height:145px;border-radius:50%;top:-74px;left:50%;margin-left:-72px;background:radial-gradient(circle at 50% 40%,#c9a58f,#7c6151);border:3px solid #fff}
.member h3{position:absolute;top:100px;width:100%;text-align:center;font-size:16px;font-weight:500}
.member p{position:absolute;top:128px;left:18px;right:18px;text-align:center;font-size:10.5px;line-height:16px;color:#333}
/* charts */
.data{background:var(--teal)}
.data h2{position:absolute;left:0;width:1152px;top:72px;text-align:center;font-size:36px;font-weight:500;color:#12231c}
.bar{bottom:90px;border:2px solid var(--gold);font-size:11px;text-align:center;padding-top:14px;color:#fff}
.axis{left:60px;top:557px;width:490px;height:4px;background:var(--gold)}
.tick{top:570px;width:30px;text-align:center;font-size:11px;color:#fff}
.item{left:628px;width:356px;height:63px}
.num{left:0;top:0;width:63px;height:63px;border:2px solid var(--gold);color:#fff;font-size:26px;text-align:center;line-height:59px}
.item h4{position:absolute;left:80px;top:-4px;font-size:19px;font-weight:400;color:#fff}
.item p{position:absolute;left:80px;top:22px;font-size:11.5px;line-height:16px;color:#d8f2ea}
.item .rule{position:absolute;left:63px;right:0;bottom:0;height:2px;background:var(--gold)}
/* timeline */
.tl-title{left:0;width:1152px;top:58px;text-align:center;font-size:40px;font-weight:500;color:var(--teal)}
.tl-intro{left:110px;width:932px;top:134px;text-align:center;font-size:15.5px;line-height:22px;color:#222}
.tl-line{left:0;top:265px;width:1152px;height:9px;background:var(--gold)}
.stem{width:2px;background:var(--teal)}
.year{width:142px;height:133px;background:var(--teal);color:#fff;text-align:center}
.year b{display:block;font-size:26px;font-weight:500;margin-top:12px}
.year span{display:block;font-size:10.5px;line-height:12px;margin:8px 10px 0;color:#e9f9f6}
/* contact */
.thanks{left:63px;top:50px;font-size:62px;font-weight:600;color:var(--teal)}
.contact-wave{left:0;top:170px;width:520px;height:120px;background:linear-gradient(180deg,rgba(179,154,85,0),rgba(179,154,85,.2),rgba(179,154,85,0))}
.company{left:60px;top:296px;font-size:25px;font-weight:500;color:var(--teal)}
.contact{left:60px;font-size:19px;color:#222;display:flex;gap:12px;line-height:26px}
.contact svg{flex:none;margin-top:5px}
.ring{left:470px;top:-40px;width:774px;height:774px;border-radius:50%;border:42px solid var(--teal);background:#fff}
</style>
</head>
<body>

<!-- Cover -->
<section class="slide" style="top:75px">
  <div class="abs cover-band"></div>
  <div class="abs cover-top"></div>
  <div class="abs cover-wave" role="img" aria-label="Fine golden flowing line decoration"></div>
  <div class="abs" style="left:160px;top:112px">
    <span class="brand-dot" style="width:40px;height:40px;margin-right:14px"></span><span class="brand" style="font-size:62px;vertical-align:middle">Kalvoren</span>
    <div class="brand-sub" style="font-size:17px;margin:2px 0 0 252px">CONSULTING</div>
  </div>
  <div class="abs welcome">WELCOME TO<strong>KALVOREN CONSULTING</strong></div>
  <div class="abs cover-photo" role="img" aria-label="Teal-toned photo of two consultants in a meeting"></div>
</section>

<!-- About -->
<section class="slide" style="top:766px">
  <div class="abs about-bg" role="img" aria-label="Teal-toned photo of glass office towers"></div>
  <div class="abs about-card"></div>
  <div class="abs skyline" role="img" aria-label="Golden city skyline illustration"></div>
  <div class="abs about-box">
    <span class="abs brand-dot" style="width:26px;height:26px;left:530px;top:14px"></span>
    <span class="abs brand-dot" style="width:26px;height:26px;right:50px;top:18px"></span>
    <h2>About <span>Our Company</span></h2>
    <p>The ever- increasing demands in terms of social, ecological and economic concerns have been presenting companies with growing challenges for years. Not only do the increasing legal requirements speak in favor of actively shaping one's own future , but also the increasing demand from consumers for sustainable products and the increasing interest of employees in sustainable aspects of corporate culture . The complexity of sustainability offers long-term solutions for sustainable business.</p>
  </div>
</section>

<!-- Team -->
<section class="slide" style="top:1456px">
  <div class="abs" style="left:0;width:1152px;top:60px;text-align:center"><span class="brand-dot" style="width:28px;height:28px"></span></div>
  <div class="abs team-band">Our Team</div>
  <div class="abs member" style="left:88px">
    <div class="abs avatar" role="img" aria-label="Portrait photo of team member"></div>
    <h3>Dr Mara Feldt</h3>
    <p>Mara is co-founder and managing director of Kalvoren Consulting GmbH. She brings strong analytical skills, thinks far ahead and keeps an overview of the essential issues. Mara is passionate about sustainability and inspires others with her friendly nature.</p>
  </div>
  <div class="abs member" style="left:440px">
    <div class="abs avatar" role="img" aria-label="Portrait photo of team member"></div>
    <h3>Dr Lena Ostrow</h3>
    <p>Lena is co-founder and managing director of Kalvoren Consulting GmbH. She excels at grasping complex issues and reducing them to the essentials. She thinks with foresight and develops target group-oriented solutions.</p>
  </div>
  <div class="abs member" style="left:798px">
    <div class="abs avatar" role="img" aria-label="Portrait photo of team member"></div>
    <h3>Dr Clara Imhof-Berg</h3>
    <p>Clara is co-founder and managing director of Kalvoren Consulting GmbH. She reacts pragmatically to changing customer needs in dynamic project settings, keeps the essentials in sight and explains complex issues in a way that suits the target group.</p>
  </div>
</section>

<!-- Data charts -->
<section class="slide data" style="top:2146px">
  <span class="abs brand-dot" style="left:62px;top:60px;width:30px;height:30px;background:#fff"></span>
  <h2>Data Charts</h2>
  <div class="abs bar" style="left:113px;width:66px;height:266px;background:var(--g1)">50%</div>
  <div class="abs bar" style="left:188px;width:66px;height:306px;background:var(--g2)">60%</div>
  <div class="abs bar" style="left:264px;width:67px;height:397px;background:var(--g3)">80%</div>
  <div class="abs bar" style="left:341px;width:66px;height:233px;background:var(--g4)">40%</div>
  <div class="abs bar" style="left:417px;width:67px;height:324px;background:var(--g5);color:#333">70%</div>
  <div class="abs axis"></div>
  <div class="abs tick" style="left:131px">1</div>
  <div class="abs tick" style="left:206px">2</div>
  <div class="abs tick" style="left:283px">3</div>
  <div class="abs tick" style="left:359px">4</div>
  <div class="abs tick" style="left:435px">5</div>
  <div class="abs item" style="top:176px"><div class="abs num" style="background:var(--g1)">1</div><h4>Heading 1</h4><p>Lorem ipsum dolor sit amet, consectetur adipiscing elit,<br>sed do eiusmod tempor incididunt ut labore et dolore</p><div class="rule"></div></div>
  <div class="abs item" style="top:256px"><div class="abs num" style="background:var(--g2)">2</div><h4>Heading 2</h4><p>Lorem ipsum dolor sit amet, consectetur adipiscing elit,<br>sed do eiusmod tempor incididunt ut labore et dolore</p><div class="rule"></div></div>
  <div class="abs item" style="top:336px"><div class="abs num" style="background:var(--g3)">3</div><h4>Heading 3</h4><p>Lorem ipsum dolor sit amet, consectetur adipiscing elit,<br>sed do eiusmod tempor incididunt ut labore et dolore</p><div class="rule"></div></div>
  <div class="abs item" style="top:417px"><div class="abs num" style="background:var(--g4)">4</div><h4>Heading 4</h4><p>Lorem ipsum dolor sit amet, consectetur adipiscing elit,<br>sed do eiusmod tempor incididunt ut labore et dolore</p><div class="rule"></div></div>
  <div class="abs item" style="top:497px"><div class="abs num" style="background:var(--g5);color:#333">5</div><h4>Heading 5</h4><p>Lorem ipsum dolor sit amet, consectetur adipiscing elit,<br>sed do eiusmod tempor incididunt ut labore et dolore</p><div class="rule"></div></div>
</section>

<!-- Timeline -->
<section class="slide" style="top:2836px">
  <span class="abs brand-dot" style="left:62px;top:58px;width:34px;height:34px"></span>
  <div class="abs tl-title">Timeline</div>
  <p class="abs tl-intro">Lorem ipsum dolor sit amet, consectetur adipiscing elit, sed do eiusmod tempor incididunt ut labore et dolore magna aliqua. Quis ipsum suspendisse ultrices gravida. Risus commodo viverra maecenas accumsan lacus vel facilisis. Lorem ipsum dolor sit amet, consectetur adipiscing elit, sed do eiusmod tempor incididunt ut labore et dolore magna aliqua. Quis ipsum suspendisse ultrices gravida.</p>
  <div class="abs tl-line"></div>
  <div class="abs stem" style="left:141px;top:274px;height:57px"></div>
  <div class="abs stem" style="left:285px;top:274px;height:156px"></div>
  <div class="abs stem" style="left:429px;top:274px;height:57px"></div>
  <div class="abs stem" style="left:572px;top:274px;height:156px"></div>
  <div class="abs stem" style="left:717px;top:274px;height:57px"></div>
  <div class="abs stem" style="left:859px;top:274px;height:156px"></div>
  <div class="abs stem" style="left:1002px;top:274px;height:57px"></div>
  <div class="abs year" style="left:71px;top:331px"><b>2016</b><span>Lorem ipsum dolor sit amet, consectetur adipiscing elit, sed do eiusmod tempor incididunt ut labore et dolore magna aliqua.</span></div>
  <div class="abs year" style="left:215px;top:430px"><b>2017</b><span>Lorem ipsum dolor sit amet, consectetur adipiscing elit, sed do eiusmod tempor incididunt ut labore et dolore magna aliqua.</span></div>
  <div class="abs year" style="left:359px;top:331px"><b>2018</b><span>Lorem ipsum dolor sit amet, consectetur adipiscing elit, sed do eiusmod tempor incididunt ut labore et dolore magna aliqua.</span></div>
  <div class="abs year" style="left:502px;top:430px"><b>2019</b><span>Lorem ipsum dolor sit amet, consectetur adipiscing elit, sed do eiusmod tempor incididunt ut labore et dolore magna aliqua.</span></div>
  <div class="abs year" style="left:647px;top:331px"><b>2020</b><span>Lorem ipsum dolor sit amet, consectetur adipiscing elit, sed do eiusmod tempor incididunt ut labore et dolore magna aliqua.</span></div>
  <div class="abs year" style="left:789px;top:430px"><b>2021</b><span>Lorem ipsum dolor sit amet, consectetur adipiscing elit, sed do eiusmod tempor incididunt ut labore et dolore magna aliqua.</span></div>
  <div class="abs year" style="left:932px;top:331px"><b>2022</b><span>Lorem ipsum dolor sit amet, consectetur adipiscing elit, sed do eiusmod tempor incididunt ut labore et dolore magna aliqua.</span></div>
</section>

<!-- Contact -->
<section class="slide" style="top:3528px">
  <div class="abs ring"></div>
  <div class="abs" style="left:620px;top:290px;width:490px;text-align:center">
    <div class="brand" style="font-size:98px">Kalvoren</div>
    <div class="brand-sub" style="font-size:30px;margin-top:6px">CONSULTING</div>
  </div>
  <div class="abs thanks">Thank You</div>
  <div class="abs contact-wave" role="img" aria-label="Fine golden flowing line decoration"></div>
  <div class="abs company">KALVOREN CONSULTING GMBH</div>
  <div class="abs contact" style="top:348px"><svg width="16" height="16" viewBox="0 0 16 16"><path d="M3 1l3 3-2 2c1 2 3 4 5 5l2-2 3 3-2 2C7 14 2 9 1 3z" fill="none" stroke="var(--teal)" stroke-width="1.4"/></svg>+49 (0) 5550 – 100 2040</div>
  <div class="abs contact" style="top:402px"><svg width="16" height="16" viewBox="0 0 16 16"><circle cx="8" cy="8" r="6.5" fill="none" stroke="var(--teal)" stroke-width="1.4"/><path d="M1.5 8h13M8 1.5c-3 3-3 10 0 13M8 1.5c3 3 3 10 0 13" fill="none" stroke="var(--teal)" stroke-width="1.2"/></svg>www.kalvoren-consulting.example</div>
  <div class="abs contact" style="top:456px"><svg width="16" height="16" viewBox="0 0 16 16"><rect x="1" y="3" width="14" height="10" fill="none" stroke="var(--teal)" stroke-width="1.4"/><path d="M1 3l7 6 7-6" fill="none" stroke="var(--teal)" stroke-width="1.4"/></svg>info@kalvoren-consulting.example</div>
  <div class="abs contact" style="top:510px"><svg width="16" height="18" viewBox="0 0 16 18"><path d="M8 17S2 10 2 6.5a6 6 0 0112 0C14 10 8 17 8 17z" fill="var(--teal)"/><circle cx="8" cy="6.5" r="2" fill="#fff"/></svg><span>Lindenhof Office Park<br>Ahornweg 12<br>12345 Musterstadt</span></div>
</section>

</body>
</html>
```